Geschäftspapiere für Bauunternehmen
Zielgruppe
Wir sind ein Bauunternehmen.
Aufgabenstellung
Bitte das Briefpapier alles nötige für eine Angebotserstellung sowie Rechnungsstellung hinzufügen. Heißt: Logo, Firma, Firmensitz, Telefonnummer, Steuernummer und Bankdaten. Bankdaten: DE41 5807 1143 2296 0183 77 BIC: TRWKDEFFXXX

```html
<!DOCTYPE html>
<html lang="de">
<head>
<meta charset="utf-8">
<title>Brenner Bau – Briefpapier</title>
<link href="https://fonts.googleapis.com/css2?family=Montserrat:wght@400;500;600&display=swap" rel="stylesheet">
<style>
  :root {
    --paper: #e3e3e3;
    --ink: #1c1c1c;
    --accent: #c8000a;
    --signature-fill: #d6d6d6;
  }
  html, body {
    margin: 0;
    padding: 0;
    overflow: hidden;
    background: var(--paper);
  }
  .letterhead {
    position: relative;
    width: 949px;
    height: 1200px;
    background: var(--paper);
    color: var(--ink);
    font-family: "Montserrat", sans-serif;
    overflow: hidden;
  }
  .letterhead > * {
    position: absolute;
    margin: 0;
    line-height: 1;
  }
  .letterhead p { margin: 0; line-height: 1; }

  .brand {
    left: 52px;
    top: 196px;
    display: flex;
    align-items: center;
    gap: 12px;
  }
  .brand-mark {
    width: 28px;
    height: 28px;
    background: var(--accent);
  }
  .brand-name {
    font-size: 38px;
    font-weight: 500;
    letter-spacing: 0.3px;
  }
  .header-rule {
    left: 52px;
    top: 234px;
    width: 820px;
    height: 2px;
    background: var(--ink);
  }

  .contact {
    left: 52px;
    top: 321px;
    font-size: 17.5px;
    font-style: normal;
  }
  .contact .address-line + .address-line { margin-top: -1px; }
  .contact .phone { margin-top: 11px; font-size: 19px; }
  .contact .email { margin-top: 10px; font-size: 18.5px; }
  .contact .tax-number { margin-top: 10px; font-size: 17.5px; }

  .company {
    right: 74px;
    top: 311px;
  }
  .company-name {
    font-size: 35px;
    font-weight: 600;
  }
  .company-type {
    font-size: 18.5px;
    margin: 5px 0 0 1px !important;
  }

  .letter-body {
    left: 52px;
    top: 521px;
    font-size: 19px;
  }
  .letter-body .message { margin-top: 32px; }
  .letter-body .closing { margin-top: 32px; line-height: 26px !important; }

  .service-note {
    left: 56px;
    top: 857px;
    font-size: 18.5px;
  }
  .service-closing {
    left: 56px;
    top: 897px;
    font-size: 18.5px;
  }
  .signature {
    left: 58px;
    top: 976px;
    width: 238px;
    height: 44px;
    background: var(--signature-fill);
  }
  .signature-role {
    left: 56px;
    top: 1047px;
    font-size: 18.5px;
  }
  .opening-hours {
    left: 54px;
    top: 1105px;
    font-size: 19px;
  }
  .bank-details {
    left: 594px;
    top: 1105px;
    font-size: 18.5px;
  }
  .bank-details .bic { margin-top: 9px; }
</style>
</head>
<body>
<main class="letterhead">
  <div class="brand">
    <span class="brand-mark"></span>
    <span class="brand-name">BRENNER BAU</span>
  </div>
  <div class="header-rule"></div>

  <address class="contact">
    <p class="address-line">Lindenauer Weg 42,</p>
    <p class="address-line">13407 Berlin, Germany</p>
    <p class="phone">030 512 77 408</p>
    <p class="email">info@brenner-bau.de</p>
    <p class="tax-number">St.-Nr.: 30/418/52736</p>
  </address>

  <div class="company">
    <p class="company-name">Brenner Bau</p>
    <p class="company-type">Bauunternehmen</p>
  </div>

  <section class="letter-body">
    <p class="salutation">Guten Tag,</p>
    <p class="message">anliegend übersende ich Ihnen die Bestätigung Ihrer Gewerbeanmeldung.</p>
    <p class="closing">Mit freundlichen Grüßen<br>im Auftrag<br>Kessler</p>
  </section>

  <p class="service-note">Wir sind gern für Sie da. Wir schätzen unsere Kunden sehr.</p>
  <p class="service-closing">Mit freundlichen Grüßen</p>

  <div class="signature" role="img" aria-label="Handschriftliche Unterschrift Brenner Bau"></div>
  <p class="signature-role">Bauunternehmen</p>

  <p class="opening-hours">Montag bis Freitag von 08.00-17.00 Uhr</p>
  <div class="bank-details">
    <p class="iban">DE41 5807 1143 2296 0183 77</p>
    <p class="bic">BIC: TRWKDEFFXXX</p>
  </div>
</main>
</body>
</html>
```